we need a business card as well as a logo that can be used for signs etc.
this is a very formal, classy , elegant function centre, as well as café. I am after a design that stands out and grabs people attentions. my colours theme is really warm ,colours like chocolate browns, and latte type colours with really deep red tones
not bright red, just warm tones. this is a place that very wealthy and maybe even celebs will come so I need it to be appealing.
Industry/Entity Type
Business
Contact Information for Business Card
Blue Fern
café and function centre @ hallam orchard.
wedding and function specialists,
Barrow parkway, lucknow,ph 0438157240

```html
<!DOCTYPE html>
<html lang="en">
<head>
<meta charset="utf-8">
<title>Blue Fern — Business Cards</title>
<link href="https://fonts.googleapis.com/css2?family=Almendra:ital,wght@0,400;0,700;1,400&display=swap" rel="stylesheet">
<style>
  :root {
    --page-bg: #d9d6d2;
    --card-top: #5a4132;
    --card-bottom: #2c1f18;
    --deep-red: #c41f26;
    --latte: #eadfb6;
    --latte-soft: #f3e9c4;
  }
  * { margin: 0; padding: 0; box-sizing: border-box; }
  html, body {
    width: 1200px;
    height: 1000px;
    overflow: hidden;
    background: var(--page-bg);
  }
  .sheet {
    width: 1200px;
    height: 1000px;
    display: flex;
    flex-direction: column;
    align-items: center;
    justify-content: center;
    gap: 50px;
  }
  .card {
    width: 720px;
    height: 410px;
    background: linear-gradient(170deg, var(--card-top) 0%, var(--card-bottom) 100%);
    box-shadow: 0 10px 24px rgba(0,0,0,0.3);
    display: flex;
    flex-direction: column;
    align-items: center;
    text-align: center;
    font-family: "Almendra", Georgia, serif;
  }
  .brand-disc {
    width: 150px;
    height: 150px;
    border-radius: 50%;
    background: var(--latte);
    margin-top: 40px;
    box-shadow: 0 4px 10px rgba(0,0,0,0.35);
  }
  .brand-name {
    color: var(--deep-red);
    font-weight: 700;
    font-size: 56px;
    line-height: 1;
    margin-top: 22px;
    letter-spacing: 1px;
  }
  .front .venue {
    color: var(--deep-red);
    font-size: 30px;
    line-height: 1.25;
    margin-top: 16px;
    text-shadow: 0 2px 3px rgba(0,0,0,0.5);
  }
  .back .brand-disc { width: 130px; height: 130px; margin-top: 30px; }
  .back .brand-name { font-size: 50px; margin-top: 18px; }
  .back .tagline {
    color: var(--latte);
    font-style: italic;
    font-size: 24px;
    letter-spacing: 1px;
    margin-top: 12px;
  }
  .contact {
    margin-top: 26px;
    font-size: 27px;
    line-height: 1.3;
    letter-spacing: 1.5px;
    text-shadow: 0 2px 3px rgba(0,0,0,0.5);
  }
  .contact .phone { color: var(--deep-red); }
  .contact .location { color: var(--latte-soft); }
</style>
</head>
<body>
  <main class="sheet">
    <section class="card front">
      <div class="brand-disc" aria-hidden="true"></div>
      <h1 class="brand-name">Blue Fern</h1>
      <p class="venue">Café and Function Centre @ Hallam<br>Orchard, Westbrook</p>
    </section>

    <section class="card back">
      <div class="brand-disc" aria-hidden="true"></div>
      <h2 class="brand-name">Blue Fern</h2>
      <p class="tagline">Wedding and Function Specialists</p>
      <div class="contact">
        <p class="phone">Phone: 0438157240 (Westbrook)</p>
        <p class="location">Location: Barrow Parkway</p>
      </div>
    </section>
  </main>
</body>
</html>
```